Verdal Group Business Card Design

The CEO is looking for a new trendy look for his business card.
You can stay with current branding or come up with something new/creative. It can be 3D, including Medical Office buildings. You can use our logo in a variety of colors. Please include name, title, company name, company website, email address, cell number

Target Market(s)

Real Estate Development and Construction

Industry/Entity Type

Health care real estate

Contact Information for Business Card

Rohesh Kamble, CEO M-702.418.6293 E-roheshkamble@verdal.example Address:4100 Lanyard St, Tampa, FL 33611 www.verdal.example

Other font styles liked:
• Be creative

Requirements
Must have
• Creative, trendy look
Nice to have
• Please go to our website to get a feel- www. verdal.example
Should not have
• small fonts

```html
<!DOCTYPE html>
<html lang="en">
<head>
<meta charset="utf-8">
<title>Verdal Group Business Card</title>
<link rel="stylesheet" href="https://fonts.googleapis.com/css2?family=Montserrat:wght@400;700;800&display=swap">
<style>
  :root {
    --bg: #3a3a3a;
    --card-gloss: #121212;
    --card-matte: #2b2b2b;
    --text-light: #d4d4d4;
    --logo-grey: #a8a8a8;
    --accent-red: #c3202b;
    --rule: #9a9a9a;
  }
  * { margin: 0; padding: 0; box-sizing: border-box; }
  html, body {
    width: 1200px; height: 694px; overflow: hidden;
    background: var(--bg);
    font-family: "Montserrat", Arial, sans-serif;
  }
  .canvas { position: relative; width: 1200px; height: 694px; }

  .card {
    position: absolute; top: 192px;
    width: 540px; height: 310px;
    border-radius: 22px; overflow: hidden;
    box-shadow: 0 14px 40px rgba(0,0,0,.45);
  }

  /* Back: pattern area as flat tonal fill */
  .card-back { left: 40px; background: var(--card-gloss); }
  .pattern-fill {
    position: absolute; inset: 0;
    background: linear-gradient(150deg, #7a7a7a 0%, #4a4a4a 30%, #242424 60%, #0e0e0e 100%);
  }
  .back-mark {
    position: absolute; right: 60px; top: 132px;
    color: var(--accent-red); font-weight: 800; font-size: 26px;
    line-height: 30px;
  }

  /* Front: contact details */
  .card-front { left: 620px; background: var(--card-matte); }
  .company-name {
    position: absolute; left: 30px; bottom: 36px;
    color: var(--logo-grey); font-weight: 800;
    font-size: 50px; line-height: 52px; letter-spacing: -1px;
  }
  .divider {
    position: absolute; left: 240px; top: 48px;
    width: 1px; height: 210px; background: var(--rule);
  }
  .contact {
    position: absolute; left: 256px; top: 50px;
    color: var(--text-light); font-size: 15px; line-height: 21px;
  }
  .person-name { font-weight: 700; font-size: 22px; line-height: 26px; letter-spacing: .5px; }
  .person-title { margin-bottom: 12px; }
  .address { margin-bottom: 10px; }
  .contact-line { display: flex; align-items: center; gap: 7px; line-height: 23px; }
  .contact-line svg { width: 14px; height: 14px; fill: var(--text-light); flex: none; }
</style>
</head>
<body>
<main class="canvas">
  <section class="card card-back">
    <div class="pattern-fill" role="img" aria-label="Glossy repeated company name pattern fading from grey to black"></div>
    <div class="back-mark">Verdal Group</div>
  </section>

  <section class="card card-front">
    <div class="company-name">Verdal<br>Group</div>
    <div class="divider"></div>
    <div class="contact">
      <div class="person-name">ROHESH KAMBLE</div>
      <div class="person-title">CEO</div>
      <div class="address">4100 Lanyard St<br>Tampa, FL 33611</div>
      <div class="contact-line">
        <svg viewBox="0 0 24 24" aria-hidden="true"><path d="M6.6 10.8a15 15 0 0 0 6.6 6.6l2.2-2.2c.3-.3.7-.4 1-.2 1.1.4 2.3.6 3.6.6.6 0 1 .4 1 1V20c0 .6-.4 1-1 1A17 17 0 0 1 3 4c0-.6.4-1 1-1h3.5c.6 0 1 .4 1 1 0 1.3.2 2.5.6 3.6.1.3 0 .7-.2 1z"/></svg>
        <span>702.418.6293</span>
      </div>
      <div class="contact-line">
        <svg viewBox="0 0 24 24" aria-hidden="true"><path d="M2 5h20v14H2zm2 2v.5l8 5 8-5V7l-8 5z"/></svg>
        <span>roheshkamble@verdal.example</span>
      </div>
      <div class="contact-line">
        <svg viewBox="0 0 24 24" aria-hidden="true"><path d="M12 2a10 10 0 1 0 0 20 10 10 0 0 0 0-20zm0 2c.9 0 2.2 1.8 2.8 5H9.2C9.8 5.8 11.1 4 12 4zM4.3 13a8 8 0 0 1 0-2h2.9a16 16 0 0 0 0 2zm.8 2h2.4c.3 1.4.8 2.6 1.4 3.5A8 8 0 0 1 5.1 15zm4.1 0h5.6c-.6 3.2-1.9 5-2.8 5s-2.2-1.8-2.8-5zm-.2-2a14 14 0 0 1 0-2h6a14 14 0 0 1 0 2zm5.6 5.5c.6-.9 1.1-2.1 1.4-3.5h2.4a8 8 0 0 1-3.8 3.5zM16.8 13a16 16 0 0 0 0-2h2.9a8 8 0 0 1 0 2zm-.3-4c-.3-1.4-.8-2.6-1.4-3.5A8 8 0 0 1 18.9 9zM7.5 9H5.1a8 8 0 0 1 3.8-3.5C8.3 6.4 7.8 7.6 7.5 9z"/></svg>
        <span>www.verdal.example</span>
      </div>
    </div>
  </section>
</main>
</body>
</html>
```